依頼詳細
◇サイトマップ
①Home
② MENU&PRICE
③ SALON INFO
④ PRODUCTS
⑤ COUPON
⑥ GALLERY
⑦ STAFF
⑧ MOVI
⑨ RECRUIT
⑩ CONTACT
⑪BLOG(一覧)
⑫NEWS(一覧)
⑬アクセサリー

◇優先事項
1.ユーザビリティー
2.デザイン
3.編集更新

◇効果
1.新規顧客の獲得
2.売上の向上
3.認知度向上(情報発信)

◇ターゲット
男性客は多いので、集客は女性をメインにしたい。
30~40代をメインだが、20代の人もターゲットに入る
会社員、自営業など全体的に伸ばしたい。

◇提供素材
ロゴデータなし。
店舗内装に写真はある。
動画もとっているものがある。

◇sns
フェイスブック
ツイッター
ラインアット
をしている。

◇その他アプリ
メール予約のシステムを使っている

◇デザイン
シンプル  3   複雑
単色    4~5 カラフル
暗い    4   明るい
日常    1   高級
遊び心  1~2  厳粛
未来的  1~2  伝統的
女性   1    男性

◇テイスト
モダン・アンティーク・レトロなデザインが好き
フォーマル・幻想的・神秘的・知性的はイメージと違う

◇カラー
ベースは白やクリーム系
サロンの雰囲気に合わせて茶色やその他の差し色

◇参考サイト
特に無いが、情報がしっかり発信出来るサイトがベスト。
サイトURL
http://www.velvora-style.com/
ページ数
1ページ
希望イメージ
シンプル 複雑
単色 カラフル
暗い 明るい
日常 高級
遊び心 厳粛
未来的 伝統的
女性的 男性的
希望する色
茶系、 ベースは白やクリーム系 サロンの雰囲気に合わせて茶色やその他の差し色
納品ファイル
• イラストレーター形式 (.ai)
• フォトショップ形式 (.psd)
• PNG形式 (.png)
補足説明
◇素材
1.現行のサイトに有る写真やテキストは自由に使って頂いて構いません。

2.この度素材として撮影をしているものを、ソラデポットにてダウンロードしてお使い下さい。
http://soradepot.net/download/7b2e41d09a5c8f3e6d1a2b4c9e0f57a8d6c3b1e2
パスワード kiro

3.当店にてピクスナを契約していますのでその中から使用して一旦カンプ画像を入れておいて下さい。
https://jp.pixuna-stock.com/

※その他は商用利用可能な無料のものをお使い下さい。
もう少し提案が見たいため延長させて頂きます。
もう少し提案を頂ければと思います。
何卒宜しくお願い致します。
もう少しデザインを見てみたいため延長させていただきます。
宜しくお願い致します。

ひと目見て気に入りました。

素早い対応ありがとうございました。

```html
<!DOCTYPE html>
<html lang="ja">
<head>
<meta charset="utf-8">
<title>Velvora Hair Make Studio</title>
<link rel="stylesheet" href="https://fonts.googleapis.com/css2?family=Noto+Sans+JP:wght@400;500;700&family=Lato:wght@400;700;900&family=Playfair+Display:wght@700&display=swap">
<style>
:root{
  --maroon:#4d1515;
  --maroon-deep:#3a0f0f;
  --cream:#f4efe4;
  --cream-dark:#ebe3d3;
  --gold:#bf9a4a;
  --ink:#333;
  --muted:#888;
  --line:#d9d2c4;
  --white:#fff;
}
*{box-sizing:border-box;margin:0;padding:0}
html,body{width:1200px;height:3524px;overflow:hidden}
body{font-family:"Noto Sans JP","Lato",sans-serif;color:var(--ink);background:var(--white);font-size:14px;position:relative}
a{color:inherit;text-decoration:none}
.photo{display:block}
/* header */
.site-header{height:148px;position:relative}
.header-info{position:absolute;left:40px;top:22px;font-size:11px;line-height:1.6;color:#666}
.sns-row{display:flex;gap:10px;margin-bottom:8px}
.sns-dot{width:18px;height:18px;background:#7aa8c7;border-radius:3px}
.sns-dot.alt{background:#55709f}
.brand{position:absolute;left:50%;top:34px;transform:translateX(-50%);text-align:center}
.brand-mark{width:34px;height:34px;border-radius:50%;background:var(--gold);margin:0 auto 6px}
.brand-name{font-family:"Playfair Display",serif;font-size:32px;color:var(--maroon);line-height:1}
.brand-sub{font-size:11px;letter-spacing:2px;color:var(--gold);margin-top:4px}
.header-contact{position:absolute;right:40px;top:20px;text-align:right}
.header-contact small{font-size:11px;color:#666}
.tel{display:flex;align-items:center;justify-content:flex-end;gap:8px;font-family:"Lato",sans-serif;font-weight:900;font-size:30px;color:var(--maroon);margin:4px 0 8px}
.reserve-btn{display:inline-block;background:var(--maroon);color:#fff;font-size:14px;padding:10px 26px;font-weight:500}
/* nav */
.global-nav{height:40px;background:var(--cream);border-top:1px solid var(--line);border-bottom:1px solid var(--line);display:flex;justify-content:center;gap:0}
.global-nav a{font-family:"Lato",sans-serif;font-size:12px;font-weight:700;line-height:40px;padding:0 22px;border-left:1px solid var(--line);color:#444}
.global-nav a:last-child{border-right:1px solid var(--line)}
/* hero */
.hero{height:452px;background:linear-gradient(160deg,#c9c0b6 0%,#efe9e2 35%,#8c4b46 60%,#d7cdc4 100%)}
.thumb-strip{display:flex;height:180px}
.thumb-strip .photo{flex:1;border-right:2px solid #fff}
.thumb-strip .photo:nth-child(odd){background:linear-gradient(135deg,#a48c78,#e2d6c8)}
.thumb-strip .photo:nth-child(even){background:linear-gradient(135deg,#6d3d36,#c7a991)}
/* concept */
.concept{height:640px;background:var(--cream);padding-top:80px}
.concept-card{width:880px;height:480px;margin:0 auto;background:#fff;display:flex;padding:0}
.concept-photo{width:430px;height:480px;background:linear-gradient(160deg,#f6f3ee,#cbb7a6 60%,#7b3a35)}
.concept-body{padding:40px 40px}
.sec-label{font-family:"Lato",sans-serif;font-weight:900;font-size:18px;letter-spacing:2px;border-left:4px solid var(--maroon);padding-left:12px}
.point-list{list-style:none;margin:26px 0 24px}
.point-list li{font-size:14px;font-weight:700;margin-bottom:12px;padding-left:18px;position:relative}
.point-list li::before{content:"";position:absolute;left:0;top:6px;width:8px;height:8px;background:var(--maroon)}
.concept-body p{font-size:12px;line-height:2;color:#666;margin-bottom:28px}
.btn-dark{display:inline-block;background:var(--maroon);color:#fff;font-size:12px;padding:10px 28px;font-family:"Lato",sans-serif}
.btn-outline{display:inline-block;border:1px solid #999;font-size:12px;padding:10px 28px;color:#555;background:#fff}
/* gallery */
.gallery{height:480px;text-align:center;padding-top:40px}
.sec-title{font-family:"Lato",sans-serif;font-weight:900;font-size:22px;letter-spacing:4px}
.circle-row{display:flex;justify-content:center;gap:28px;margin:56px 0 70px}
.circle-row .photo{width:162px;height:162px;border-radius:50%;background:linear-gradient(160deg,#d9cabb,#7a5440)}
/* staff */
.staff{height:220px;background:var(--maroon);display:flex;color:#fff}
.staff-head{width:300px;padding:50px 0 0 40px}
.staff-head .sec-label{border-color:#fff;color:#fff}
.staff-head .btn-outline{background:transparent;color:#fff;border-color:#fff;margin-top:30px}
.staff-owner{width:260px;position:relative;background:linear-gradient(120deg,#3a0f0f,#6a3328)}
.owner-label{position:absolute;left:130px;top:70px;font-size:12px}
.owner-label strong{display:block;font-size:24px;margin-top:6px}
.owner-label small{display:block;font-size:9px;color:#e8cfcf}
.staff-photos{flex:1;display:flex}
.staff-photos .photo{flex:1;background:linear-gradient(150deg,#b79d88,#4a2820)}
.staff-photos .photo:nth-child(2){background:linear-gradient(150deg,#d8c7b4,#7b5b47)}
/* blog */
.blog{height:440px;background:var(--cream);padding:70px 160px 0}
.sec-row{display:flex;justify-content:space-between;align-items:center}
.card-row{display:flex;gap:20px;margin-top:36px}
.blog-card{flex:1}
.blog-card .photo{height:120px;position:relative}
.blog-card:nth-child(1) .photo{background:linear-gradient(150deg,#f2b25f,#7b4a2c)}
.blog-card:nth-child(2) .photo{background:linear-gradient(150deg,#6f7a4a,#c9a568)}
.blog-card:nth-child(3) .photo{background:linear-gradient(150deg,#4a3a33,#c1a28a)}
.blog-card:nth-child(4) .photo{background:linear-gradient(150deg,#cfd7b6,#b13a30)}
.tag{position:absolute;left:0;top:0;background:#c0392b;color:#fff;font-size:10px;padding:3px 8px}
.blog-card p{background:#fff;font-size:12px;padding:10px;color:#555}
/* news + feed */
.news-area{height:360px;display:flex;gap:40px;padding:60px 160px 0}
.news{flex:1}
.news-list{list-style:none;margin-top:20px}
.news-list li{display:flex;gap:28px;font-size:12px;color:#555;padding:10px 0;border-bottom:1px dotted var(--line)}
.news-list time{font-family:"Lato",sans-serif;color:var(--muted)}
.feed{width:290px}
.feed-box{margin-top:20px;border:1px solid var(--line);height:210px;padding:10px;font-size:12px;color:#555}
.feed-photo{height:64px;background:linear-gradient(120deg,#4d1515,#bf9a4a)}
.feed-box p{margin-top:10px;line-height:1.6;word-break:break-all}
/* info */
.salon-info{height:260px;display:flex;gap:40px;padding:30px 160px 0;border-top:1px solid var(--line)}
.info-table{flex:1;border-collapse:collapse;font-size:12px}
.info-table th{width:90px;text-align:left;font-weight:400;color:var(--muted);padding:6px 0;vertical-align:top}
.info-table td{padding:6px 0;color:#444}
.map{width:430px;height:190px;background:linear-gradient(135deg,#e8e6df,#d4dcd2)}
/* footer */
.site-footer{height:200px;background:var(--maroon);padding:34px 160px 0;color:#fff}
.footer-nav{display:grid;grid-template-columns:repeat(6,1fr);row-gap:14px;font-size:11px;font-family:"Lato",sans-serif}
.footer-nav a::before{content:"› ";}
.copy{font-size:10px;color:#c9a5a5;text-align:right;margin-top:50px}
.foot-sns{display:flex;gap:10px;padding:36px 40px}
.pagetop{position:absolute;right:40px;top:3440px;width:34px;height:34px;background:var(--maroon)}
</style>
</head>
<body>
<header class="site-header">
  <div class="header-info">
    <div class="sns-row"><span class="sns-dot"></span><span class="sns-dot alt"></span></div>
    〒550-0000<br>大阪市中央区南花町1丁目2-3 花町ビル1F<br>営業 10:00〜20:00<br>› 最寄り駅から徒歩3分
  </div>
  <a class="brand" href="#">
    <div class="brand-mark"></div>
    <div class="brand-name">Velvora</div>
    <div class="brand-sub">Hair Make Studio</div>
  </a>
  <div class="header-contact">
    <small>ヘアサロンへのご予約はこちら</small>
    <div class="tel">
      <svg width="22" height="22" viewBox="0 0 24 24"><path fill="#4d1515" d="M6.6 10.8a15 15 0 0 0 6.6 6.6l2.2-2.2c.3-.3.7-.4 1-.2 1.1.4 2.3.6 3.6.6.6 0 1 .4 1 1V20c0 .6-.4 1-1 1A17 17 0 0 1 3 4c0-.6.4-1 1-1h3.5c.6 0 1 .4 1 1 0 1.3.2 2.5.6 3.6.1.3 0 .7-.2 1z"/></svg>
      06-4812-3390
    </div>
    <a class="reserve-btn" href="#">ネットでサロン予約</a>
  </div>
</header>
<nav class="global-nav">
  <a href="#">HOME</a><a href="#">CONCEPT</a><a href="#">SALON INFO</a><a href="#">MENU&amp;PRICE</a><a href="#">PRODUCTS</a><a href="#">GALLERY</a><a href="#">STAFF</a><a href="#">MOVIE</a><a href="#">NEWS</a><a href="#">BLOG</a>
</nav>
<div class="hero photo" role="img" aria-label="サロン外観の看板写真"></div>
<div class="thumb-strip">
  <div class="photo" role="img" aria-label="店内の小物写真"></div>
  <div class="photo" role="img" aria-label="アンティーク時計の写真"></div>
  <div class="photo" role="img" aria-label="カラフルな雑貨の写真"></div>
  <div class="photo" role="img" aria-label="店内装飾の写真"></div>
  <div class="photo" role="img" aria-label="ボトル類の写真"></div>
  <div class="photo" role="img" aria-label="店内ディスプレイの写真"></div>
  <div class="photo" role="img" aria-label="ヘアケア商品の写真"></div>
  <div class="photo" role="img" aria-label="オブジェの写真"></div>
</div>
<section class="concept">
  <div class="concept-card">
    <div class="concept-photo photo" role="img" aria-label="明るいサロン店内の写真"></div>
    <div class="concept-body">
      <h2 class="sec-label">CONCEPT</h2>
      <ul class="point-list">
        <li>初心者ヘアケア知識と髪にやさしい厳選された薬剤</li>
        <li>誰もが通いやすいお店</li>
        <li>お客様にフィットするスタイル</li>
        <li>最新3D頭皮エステ</li>
      </ul>
      <p>ひとりひとりの髪と向き合い、毎日が楽しくなるスタイルをご提案します。居心地のよい空間で、ゆっくりとした時間をお過ごしください。季節に合わせたケアもお任せください。</p>
      <a class="btn-dark" href="#">CONCEPT　›</a>
    </div>
  </div>
</section>
<section class="gallery">
  <h2 class="sec-title">GALLERY</h2>
  <div class="circle-row">
    <div class="photo" role="img" aria-label="ヘアスタイル作品1"></div>
    <div class="photo" role="img" aria-label="ヘアスタイル作品2"></div>
    <div class="photo" role="img" aria-label="ヘアスタイル作品3"></div>
    <div class="photo" role="img" aria-label="ヘアスタイル作品4"></div>
    <div class="photo" role="img" aria-label="ヘアスタイル作品5"></div>
    <div class="photo" role="img" aria-label="ヘアスタイル作品6"></div>
  </div>
  <a class="btn-outline" href="#">GALLERY一覧 ›</a>
</section>
<section class="staff">
  <div class="staff-head">
    <h2 class="sec-label">STAFF</h2>
    <a class="btn-outline" href="#">STAFF一覧 ›</a>
  </div>
  <div class="staff-owner photo" role="img" aria-label="オーナーの写真">
    <div class="owner-label">Owner<small>Kenji Morita</small><strong>森田 健二</strong></div>
  </div>
  <div class="staff-photos">
    <div class="photo" role="img" aria-label="スタッフの写真"></div>
    <div class="photo" role="img" aria-label="スタッフの写真"></div>
    <div class="photo" role="img" aria-label="スタッフの写真"></div>
  </div>
</section>
<section class="blog">
  <div class="sec-row"><h2 class="sec-title">BLOG</h2><a class="btn-outline" href="#">BLOG一覧 ›</a></div>
  <div class="card-row">
    <article class="blog-card"><div class="photo" role="img" aria-label="夕景の写真"><span class="tag">カテゴリー</span></div><p>春の新作スタイルのご紹介…</p></article>
    <article class="blog-card"><div class="photo" role="img" aria-label="並木道の写真"><span class="tag">カテゴリー</span></div><p>季節のヘアケアについて…</p></article>
    <article class="blog-card"><div class="photo" role="img" aria-label="ヘアアレンジの写真"><span class="tag">カテゴリー</span></div><p>簡単アレンジのコツ…</p></article>
    <article class="blog-card"><div class="photo" role="img" aria-label="スクーターの写真"><span class="tag">カテゴリー</span></div><p>休日のおでかけ日記…</p></article>
  </div>
</section>
<section class="news-area">
  <div class="news">
    <div class="sec-row"><h2 class="sec-label">NEWS</h2><a class="btn-outline" href="#">NEWS一覧 ›</a></div>
    <ul class="news-list">
      <li><time>2017.02.01</time>2月の営業日のお知らせです</li>
      <li><time>2017.01.25</time>新しいスタッフが仲間入りしました</li>
      <li><time>2017.01.18</time>ヘアケア新商品の取り扱い開始</li>
      <li><time>2017.01.10</time>冬季限定クーポンのご案内</li>
      <li><time>2017.01.04</time>本年もよろしくお願いいたします</li>
    </ul>
  </div>
  <div class="feed">
    <h2 class="sec-label">SNS FEED</h2>
    <div class="feed-box">
      <div class="feed-photo photo" role="img" aria-label="SNS投稿の画像"></div>
      <p>http://www.velvora-style.com/blog-detail/entry/093</p>
      <p>Velvora Hair Make Studio</p>
    </div>
  </div>
</section>
<section class="salon-info">
  <table class="info-table">
    <tr><th>店名</th><td>Velvora (ヴェルヴォラ)</td></tr>
    <tr><th>住所</th><td>〒550-0000 大阪市中央区南花町1丁目2-3 花町ビル1F</td></tr>
    <tr><th>電話番号</th><td>06-4812-3390</td></tr>
    <tr><th>営業時間</th><td>平日 10:00〜20:00 ／ 土日祝 9:00〜19:00</td></tr>
    <tr><th>定休日</th><td>毎週火曜日</td></tr>
    <tr><th>席数</th><td>セット面 6席</td></tr>
  </table>
  <div class="map" role="img" aria-label="サロン周辺の地図"></div>
</section>
<footer class="site-footer">
  <nav class="footer-nav">
    <a href="#">HOME</a><a href="#">MENU&amp;PRICE</a><a href="#">SALON INFO</a><a href="#">PRODUCTS</a><a href="#">COUPON</a><a href="#">GALLERY</a>
    <a href="#">STAFF</a><a href="#">MOVIE</a><a href="#">RECRUIT</a><a href="#">NEWS</a><a href="#">BLOG</a><a href="#">アクセサリー</a>
  </nav>
  <p class="copy">Copyright © Velvora. All rights reserved.</p>
</footer>
<div class="foot-sns"><span class="sns-dot"></span><span class="sns-dot alt"></span></div>
<a class="pagetop" href="#" aria-label="ページトップへ"><svg width="34" height="34" viewBox="0 0 34 34"><path d="M11 20l6-6 6 6" fill="none" stroke="#fff" stroke-width="2"/></svg></a>
</body>
</html>
```